Specialty Contact lens for children

We need a large size canvas 24x36" to advertise specialty fit contact lens for children to control myopia. please visit our website for more about our office theme www.tandriloo.com
We want modern , fresh, happy design. Color blue, green, white. Final design should communicate the best lens choice for the children. Banner to include a picture of happy teen playing sports or out in park without glasses. To portray the new ability to see without glasses.
ORTHO-K #1 MYOPIA control treatment for children
- Corrects your vision while you sleep
- Creates crisp clear vision all day
- Freedom: No glasses, No Surgery, No soft lenses
-Safe and effective for children and adults

Target Market(s)

8-25 years old

Industry/Entity Type

Health Care

Font styles to use
Sans Serif

Colors
0692cd
cee9f5
ecf7fb
ffffff
86cfc6

Requirements
Must have
• Picture of teen playing sports or outdoors without glasses
Nice to have
• office logo on banner. happy color blue, green, white.
• Modern font: century gothic

```html
<!DOCTYPE html>
<html lang="en">
<head>
<meta charset="utf-8">
<title>Ortho-K Myopia Control Poster</title>
<link href="https://fonts.googleapis.com/css2?family=Questrial&display=swap" rel="stylesheet">
<style>
  :root {
    --blue: #1b74c0;
    --blue-bright: #0692cd;
    --blue-pale: #cee9f5;
    --ice: #ecf7fb;
    --white: #ffffff;
    --mint: #86cfc6;
    --mint-deep: #5aab9e;
    --ink: #222629;
    --grey: #5b5f62;
  }
  html, body {
    margin: 0;
    padding: 0;
    overflow: hidden;
    background: var(--white);
  }
  .poster {
    position: relative;
    width: 923px;
    height: 1200px;
    overflow: hidden;
    font-family: "Questrial", "Century Gothic", sans-serif;
    background: linear-gradient(180deg, var(--white) 0%, var(--ice) 55%, #bfe6e0 82%, #9fdad2 100%);
  }
  .art {
    position: absolute;
    left: 0;
    top: 0;
    width: 923px;
    height: 1200px;
  }
  .practice-name {
    position: absolute;
    left: 38px;
    top: 636px;
    margin: 0;
    color: var(--grey);
    font-size: 31px;
    font-weight: 400;
    letter-spacing: 2px;
    line-height: 1.15;
  }
  .headline {
    position: absolute;
    left: 40px;
    top: 752px;
    margin: 0;
    font-weight: 400;
    line-height: 1.1;
  }
  .headline-top {
    display: block;
    color: var(--mint-deep);
    font-size: 46px;
    letter-spacing: 0.5px;
  }
  .headline-sub {
    display: block;
    color: var(--blue);
    font-size: 41px;
  }
  .benefits {
    position: absolute;
    left: 38px;
    top: 882px;
    margin: 0;
    padding: 0;
    list-style: none;
  }
  .benefit {
    display: flex;
    align-items: center;
    height: 52px;
    color: var(--ink);
    font-size: 30px;
  }
  .benefit-icon {
    width: 34px;
    height: 34px;
    margin-right: 16px;
    flex: none;
  }
  .website {
    position: absolute;
    left: 0;
    width: 923px;
    top: 1138px;
    margin: 0;
    line-height: 48px;
    text-align: center;
    color: var(--white);
    font-size: 40px;
    letter-spacing: 0.5px;
  }
</style>
</head>
<body>
<main class="poster">
  <svg class="art" viewBox="0 0 923 1200" xmlns="http://www.w3.org/2000/svg">
    <defs>
      <linearGradient id="photo-tone" x1="0" y1="0" x2="1" y2="1">
        <stop offset="0" stop-color="#cfcac2"/>
        <stop offset="0.5" stop-color="#bdb8b0"/>
        <stop offset="1" stop-color="#a7a39c"/>
      </linearGradient>
      <linearGradient id="wave-blue" x1="0" y1="0" x2="1" y2="0">
        <stop offset="0" stop-color="#86cfe0"/>
        <stop offset="0.6" stop-color="#4ea6d8"/>
        <stop offset="1" stop-color="var(--blue)"/>
      </linearGradient>
    </defs>

    <path class="photo-area" role="img"
          aria-label="Photo: happy teens without glasses playing basketball on a sandy court, reaching up toward a ball above a red hoop"
          fill="url(#photo-tone)"
          d="M0 0 H923 V560 C780 690 640 640 470 540 C320 450 150 410 0 445 Z"/>

    <path class="wave-mint" fill="var(--mint)"
          d="M0 445 C150 410 320 450 470 540 C640 640 780 690 923 560 V625 C800 740 640 720 460 610 C300 500 150 455 0 458 Z"/>
    <path class="wave-blue" fill="url(#wave-blue)"
          d="M0 445 C150 410 320 450 470 540 C640 640 780 690 923 560 V595 C790 700 640 685 465 580 C310 480 150 445 0 452 Z"/>

    <path class="footer-glow" fill="var(--blue-pale)"
          d="M0 1118 C300 1080 620 1078 923 1098 V1200 H0 Z"/>
    <path class="footer-band" fill="var(--blue)"
          d="M0 1132 C300 1094 620 1092 923 1112 V1200 H0 Z"/>
  </svg>

  <p class="practice-name">TANDRILOO<br>OPTOMETRY</p>

  <h1 class="headline">
    <span class="headline-top">ORTHO-K #1 MYOPIA</span>
    <span class="headline-sub">control treatment for children</span>
  </h1>

  <ul class="benefits">
    <li class="benefit">
      <svg class="benefit-icon" viewBox="0 0 34 34" aria-hidden="true"><circle cx="17" cy="17" r="15" fill="var(--white)" stroke="var(--blue-bright)" stroke-width="2"/><path d="M14 10 L21 17 L14 24" fill="none" stroke="var(--blue)" stroke-width="3" stroke-linecap="round" stroke-linejoin="round"/></svg>
      Corrects your vision while you sleep
    </li>
    <li class="benefit">
      <svg class="benefit-icon" viewBox="0 0 34 34" aria-hidden="true"><circle cx="17" cy="17" r="15" fill="var(--white)" stroke="var(--blue-bright)" stroke-width="2"/><path d="M14 10 L21 17 L14 24" fill="none" stroke="var(--blue)" stroke-width="3" stroke-linecap="round" stroke-linejoin="round"/></svg>
      Creates crisp clear vision all day
    </li>
    <li class="benefit">
      <svg class="benefit-icon" viewBox="0 0 34 34" aria-hidden="true"><circle cx="17" cy="17" r="15" fill="var(--white)" stroke="var(--blue-bright)" stroke-width="2"/><path d="M14 10 L21 17 L14 24" fill="none" stroke="var(--blue)" stroke-width="3" stroke-linecap="round" stroke-linejoin="round"/></svg>
      Freedom: No glasses, No Surgery, No soft lenses
    </li>
    <li class="benefit">
      <svg class="benefit-icon" viewBox="0 0 34 34" aria-hidden="true"><circle cx="17" cy="17" r="15" fill="var(--white)" stroke="var(--blue-bright)" stroke-width="2"/><path d="M14 10 L21 17 L14 24" fill="none" stroke="var(--blue)" stroke-width="3" stroke-linecap="round" stroke-linejoin="round"/></svg>
      Safe and effective for children and adults
    </li>
  </ul>

  <p class="website">www.tandriloo.com</p>
</main>
</body>
</html>
```